Fixed price car insurance banner ad for insurance broker

We need a banner ad for addition to web pages and which will advertise an innovative insurance product we are selling.

We are an insurance broker and our product is a fixed price car insurance product.

The banner ad needs to display the company logo. This will be uploaded within the file upload section.

The remainder of the banner ad needs to explain what we are offering and also include the gear stick picture for impact.

We would like to see colours that tie in with the corporate colours, or alternative are striking and have presence on even the busiest web page I.e. Black banner and silver / white text. Please see the file upload for a sample of the brochure we are preparing for this product.

Target Market(s)

Private and commercial clients with both regular and high value motor vehicles.

Industry/Entity Type

Car Insurance

Font styles to use
Serif
Sans Serif

Colors

Designer to choose colors to be used in the design.

Requirements
Must have
• The banner must have the company logo on both pages.

I would like the advert to scroll / roll / fade or other between two pages displaying the following text:

Page 1
"Motor Insurance Scheme"
"Anything But Standard"
and including the gear knob picture

Page 2
Any Driver, Any Car, No Forms and One Flat Premium*

On clicking the banner ad, this will open an email, pre populated with email contact to request more detail.

Nice to have
• Open to your suggestions on this
Should not have
• Nothing at this stage. I will guide you when the ads are being submitted.

```html
<!DOCTYPE html>
<html lang="en">
<head>
<meta charset="utf-8">
<title>Motor Insurance Scheme Banner</title>
<link rel="stylesheet" href="https://fonts.googleapis.com/css2?family=Arimo:ital,wght@0,400;0,700;1,400&display=swap">
<style>
  :root {
    --ink: #000000;
    --band: #121212;
    --white: #ffffff;
    --navy: #1f2a55;
    --silver: #c9c9c9;
    --steel-light: #e6e6e6;
    --steel-dark: #3a3a3a;
  }
  html, body {
    margin: 0;
    padding: 0;
    overflow: hidden;
    background: var(--white);
  }
  .banner {
    position: relative;
    width: 1200px;
    height: 148px;
    background: var(--ink);
    overflow: hidden;
    font-family: "Arimo", Arial, sans-serif;
  }
  .brand-panel {
    position: absolute;
    left: 0;
    top: 0;
    width: 231px;
    height: 148px;
    background: var(--white);
    display: flex;
    align-items: center;
    justify-content: center;
  }
  .brand-name {
    color: var(--navy);
    font-weight: 400;
    font-size: 19px;
    letter-spacing: 3px;
    text-transform: uppercase;
    text-align: center;
    line-height: 1.5;
  }
  .title-bar {
    position: absolute;
    left: 231px;
    top: 0;
    width: 700px;
    height: 70px;
    background: var(--ink);
  }
  .headline {
    position: absolute;
    left: 244px;
    top: 12px;
    margin: 0;
    color: var(--white);
    font-weight: 700;
    font-size: 43px;
    line-height: 1;
    letter-spacing: 0.3px;
  }
  .divider {
    position: absolute;
    left: 231px;
    top: 72px;
    width: 670px;
    height: 3px;
    background: var(--silver);
  }
  .tagline-band {
    position: absolute;
    left: 231px;
    top: 78px;
    width: 680px;
    height: 70px;
    background: linear-gradient(180deg, #1c1c1c 0%, var(--band) 100%);
  }
  .tagline {
    position: absolute;
    right: 351px;
    top: 95px;
    margin: 0;
    color: var(--white);
    font-style: italic;
    font-weight: 400;
    font-size: 31px;
    line-height: 1;
  }
  .gear-visual {
    position: absolute;
    left: 900px;
    top: 0;
    width: 300px;
    height: 148px;
    background: radial-gradient(ellipse at 75% 45%, var(--steel-light) 0%, #9a9a9a 35%, var(--steel-dark) 75%, #111 100%);
  }
  .arc {
    position: absolute;
    left: 860px;
    top: 0;
  }
</style>
</head>
<body>
  <div class="banner">
    <div class="brand-panel">
      <div class="brand-name">Halden<br>Insurance</div>
    </div>
    <div class="title-bar"></div>
    <h1 class="headline">Motor Insurance Scheme</h1>
    <div class="divider"></div>
    <div class="tagline-band"></div>
    <p class="tagline">Anything But Standard</p>
    <div class="gear-visual" role="img" aria-label="Close-up photographs of a chrome gear knob and gear stick"></div>
    <svg class="arc" width="80" height="148" viewBox="0 0 80 148" aria-hidden="true">
      <path d="M60 -4 Q10 74 60 152 L80 152 L80 -4 Z" fill="#0d0d0d"/>
      <path d="M60 -4 Q10 74 60 152" fill="none" stroke="#bdbdbd" stroke-width="7"/>
    </svg>
  </div>
</body>
</html>
```